Keystone Physical Therapy needs a New website look and update!

New updated look. Most people do not know they can go directly to a physical therapist for care. Cost effective and specialized. Getting back to your life and activity is what we do. What we treat. Your first cost effective provider for pain" for example. We treat children to seniors. Theme should be warm, caring, individualized, respect your time, and cost -effective. Mobile phone ready. Encourage taking action to call and schedule to get back to life, sports, activity.
Add link to send appointment request or contact us now
Add link ( code) for patients to fill out intake form or appointment request. I want to add testimonials for other therapists.
***My current website is "brellowkeypt.net"

```html
<!DOCTYPE html>
<html lang="en">
<head>
<meta charset="utf-8">
<title>Keystone Physical Therapy</title>
<link href="https://fonts.googleapis.com/css2?family=Open+Sans:ital,wdth,wght@0,75..100,300..800;1,75..100,300..800&display=swap" rel="stylesheet">
<style>
:root{
  --green:#8cc43c;
  --blue:#3f7c9d;
  --blue-dark:#356b88;
  --ink:#333;
  --muted:#555;
  --heading-blue:#3a7397;
  --footer:#232323;
  --footer-line:#3a3a3a;
  --light:#f4f4f4;
  --white:#fff;
}
*{box-sizing:border-box;margin:0;padding:0}
html,body{width:1200px;height:3010px;overflow:hidden}
body{font-family:"Open Sans",Arial,sans-serif;color:var(--ink);background:var(--white);position:relative}
a{color:inherit;text-decoration:none}
.abs{position:absolute}

/* header */
.site-header{position:absolute;left:0;top:0;width:1200px;height:146px;background:var(--white)}
.brand{position:absolute;left:100px;top:30px;display:flex;align-items:center;gap:14px}
.brand-dot{width:84px;height:84px;border-radius:50%;background:var(--blue)}
.brand-name{font-size:40px;font-weight:700;color:var(--blue);letter-spacing:-.5px}
.header-contact{position:absolute;left:696px;top:50px;display:flex;gap:14px;align-items:center}
.header-contact .lines{border-left:1px solid #ccc;padding-left:12px;font-size:14px;color:var(--muted);line-height:24px}
.btn-contact{position:absolute;left:946px;top:52px;width:152px;height:40px;background:var(--green);color:var(--white);font-size:13px;font-weight:700;display:flex;align-items:center;justify-content:center}
.main-nav{position:absolute;left:0;top:146px;width:1200px;height:50px;background:var(--blue);display:flex;padding-left:100px}
.main-nav a{color:var(--white);font-size:13px;font-weight:600;height:50px;line-height:50px;padding:0 20px;text-transform:uppercase}
.main-nav a.active{background:var(--green);padding:0 21px}

/* hero */
.hero{position:absolute;left:0;top:196px;width:1200px;height:520px;background:radial-gradient(ellipse at 50% 45%,#6d7f8c 0%,#2b3640 45%,#0d1216 100%)}
.hero-title{position:absolute;top:70px;width:100%;text-align:center;color:var(--white);font-size:42px;font-weight:700;font-stretch:75%}
.hero-arrow{position:absolute;top:280px}
.intake-band{position:absolute;left:0;top:640px;width:1200px;height:190px}
.intake-title{position:absolute;left:122px;top:726px;color:var(--white);font-size:25px;font-weight:700}
.intake-sub{position:absolute;left:122px;top:764px;color:var(--white);font-size:15px;font-weight:600}
.btn-outline{position:absolute;left:822px;top:744px;width:246px;height:38px;border:2px solid var(--white);border-radius:20px;color:var(--white);font-size:15px;font-weight:600;display:flex;align-items:center;justify-content:center}

/* welcome */
.welcome-title{position:absolute;top:898px;width:100%;text-align:center;font-size:37px;font-weight:600;color:#444}
.welcome-title span{color:var(--heading-blue)}
.welcome-text{position:absolute;left:172px;top:956px;width:856px;text-align:center;font-size:11px;line-height:22px;color:var(--muted)}
.feature{position:absolute;top:1088px;width:318px}
.feature-img{width:318px;height:178px;border:4px solid #e6e6e6}
.feature h3{font-size:18px;font-weight:400;margin-top:20px;color:#333}
.feature p{font-size:11px;line-height:20px;color:var(--muted);margin-top:6px}

/* services */
.services{position:absolute;left:0;top:1436px;width:1200px;height:466px;background:linear-gradient(180deg,var(--blue) 0%,var(--blue-dark) 100%)}
.section-title{position:absolute;width:100%;text-align:center;font-size:31px;font-weight:500}
.services .section-title{top:64px;color:var(--white)}
.service{position:absolute;top:160px;width:230px;text-align:center;color:var(--white)}
.service svg{display:block;margin:0 auto}
.service h3{font-size:18px;font-weight:500;margin-top:14px}
.service p{font-size:11px;line-height:20px;margin-top:6px}

/* testimonials */
.testimonials{position:absolute;left:0;top:1902px;width:1200px;height:334px;background:var(--light)}
.testimonials .section-title{top:54px;color:#444}
.testimonial{position:absolute;top:144px;width:480px}
.avatar{position:absolute;left:0;top:0;width:120px;height:120px;border-radius:50%;border:4px solid #ddd;background:linear-gradient(160deg,#d9b79c,#8a6b55)}
.testimonial blockquote{position:absolute;left:140px;top:0;width:340px;font-size:11px;line-height:20px;font-style:italic;color:var(--muted)}
.testimonial .name{position:absolute;left:140px;top:80px;font-size:16px;font-style:italic;font-weight:600;color:var(--heading-blue)}
.testimonial .role{position:absolute;left:140px;top:104px;font-size:11px;font-style:italic;color:#444}
.testimonial .quote-mark{position:absolute;left:424px;top:76px;font-size:64px;font-weight:800;color:#ccc;line-height:1}

/* insurance */
.insurance-title{position:absolute;top:2318px;width:100%;text-align:center;font-size:36px;font-weight:500;color:#444}
.insurance-text{position:absolute;left:250px;top:2372px;width:700px;text-align:center;font-size:11px;line-height:22px;color:var(--muted)}
.carrier-list{position:absolute;top:2444px;list-style:none;font-size:11px;line-height:22px;color:var(--muted)}
.carrier-list li::before{content:"\203A";display:inline-block;width:10px;height:10px;line-height:10px;border-radius:50%;background:#444;color:#fff;font-size:9px;text-align:center;margin-right:10px}

/* footer */
.site-footer{position:absolute;left:0;top:2580px;width:1200px;height:430px}
.footer-col{position:absolute;top:2672px;color:var(--white)}
.footer-col h4{font-size:19px;font-weight:700;margin-bottom:22px}
.footer-col p,.footer-col li{font-size:13px;line-height:20px}
.contact-row{display:flex;gap:16px;margin-top:14px;align-items:flex-start}
.quick-links{list-style:none}
.quick-links li::before{content:"";display:inline-block;border-left:6px solid #fff;border-top:4px solid transparent;border-bottom:4px solid transparent;margin-right:12px}
.map{width:260px;height:138px;border:4px solid #fff;background:linear-gradient(135deg,#e7e4dc,#cfd9c6 60%,#bfd3e3)}
.social li{list-style:none;display:flex;align-items:center;gap:10px;margin-bottom:16px}
.social .ring{width:26px;height:26px;border:2px solid #fff;border-radius:50%}
.footer-rule{position:absolute;left:0;top:2928px;width:1200px;height:1px;background:var(--footer-line)}
.copyright{position:absolute;top:2954px;width:100%;text-align:center;font-size:11px;color:#ddd}
</style>
</head>
<body>

<header class="site-header">
  <a class="brand" href="#"><span class="brand-dot"></span><span class="brand-name">Keystone</span></a>
  <div class="header-contact">
    <svg width="26" height="34" viewBox="0 0 26 34"><path d="M6 2 L11 8 L8 13 Q11 21 17 25 L21 21 L25 27 L20 32 Q4 26 2 8 Z" fill="var(--blue)"/></svg>
    <div class="lines">info@brellowkeypt.net<br>Phone : 555-214-0187</div>
  </div>
  <a class="btn-contact" href="#">CONTACT US NOW</a>
</header>

<nav class="main-nav">
  <a class="active" href="#">Home</a><a href="#">About Us</a><a href="#">Services</a><a href="#">FAQ</a><a href="#">Form</a><a href="#">Insurance</a><a href="#">Blog</a><a href="#">Contact Us</a>
</nav>

<section class="hero" role="img" aria-label="Swimmer in a blue cap doing the butterfly stroke with water splashing on a dark background">
  <h1 class="hero-title">KEYSTONE PHYSICAL THERAPY</h1>
  <svg class="hero-arrow" style="left:40px" width="14" height="20"><path d="M11 2 L3 10 L11 18" stroke="#fff" stroke-width="3" fill="none"/></svg>
  <svg class="hero-arrow" style="left:1146px" width="14" height="20"><path d="M3 2 L11 10 L3 18" stroke="#fff" stroke-width="3" fill="none"/></svg>
</section>

<svg class="intake-band abs" viewBox="0 0 1200 190" preserveAspectRatio="none">
  <path d="M0 40 Q600 -20 1200 40 L1200 190 L0 190 Z" fill="#fff"/>
  <path d="M0 50 Q600 -8 1200 50 L1200 188 L0 188 Z" fill="var(--green)"/>
</svg>
<h2 class="intake-title">PATIENTS TO FILL OUT INTAKE FORM</h2>
<p class="intake-sub">Sed ut perspiciatis unde omnis iste natus error sit voluptatem accusantium dolore</p>
<a class="btn-outline" href="#">APPOINTMENT REQUEST</a>

<h2 class="welcome-title">Welcome To <span>Keystone Physical Therapy</span></h2>
<p class="welcome-text">Welcome to Keystone Physical Therapy, southeast Denver's choice for healing and rehabilitation. Our therapist owned practice is committed to restoration, wellness and quality of life providing compassionate, skilled care to clients of all ages. Keystone Physical Therapy treats a wide range of injuries and conditions, whether you're recovering from surgery, returning to athletics or enhancing sports performance. Partnering with you to achieve and maintain a healthy, vigorous lifestyle, our therapists deliver exceptional, progressive care in a comfortable, well-equipped environment.</p>

<article class="feature" style="left:96px">
  <div class="feature-img" role="img" aria-label="Two people stretching on exercise mats in a gym" style="background:linear-gradient(135deg,#c9a877,#8a6a48 60%,#3e5c86)"></div>
  <h3>Maintain a Healthy</h3>
  <p>Lorem ipsum dolor sit amet, consectetur adipiscing elit, sed do eiusmod tempor incididunt ut labore</p>
</article>
<article class="feature" style="left:438px">
  <div class="feature-img" role="img" aria-label="Woman in green stretching her leg on an outdoor path" style="background:linear-gradient(135deg,#8aa07a,#c8c2b4 55%,#3f8a5a)"></div>
  <h3>Vigorous Lifestyle</h3>
  <p>Lorem ipsum dolor sit amet, consectetur adipiscing elit, sed do eiusmod tempor incididunt ut labore</p>
</article>
<article class="feature" style="left:780px">
  <div class="feature-img" role="img" aria-label="Woman in pink lying on a foam roller on a blue mat" style="background:linear-gradient(135deg,#3d7fb8,#e07a9e 55%,#2d5f93)"></div>
  <h3>Physical Therapy</h3>
  <p>Lorem ipsum dolor sit amet, consectetur adipiscing elit, sed do eiusmod tempor incididunt ut labore</p>
</article>

<section class="services">
  <h2 class="section-title">THERAPY SERVICES</h2>
  <div class="service" style="left:85px">
    <svg width="112" height="112" viewBox="0 0 112 112"><circle cx="56" cy="56" r="50" fill="none" stroke="#fff" stroke-width="4"/><path d="M8 70 A50 50 0 0 0 104 70" fill="none" stroke="#fff" stroke-width="8"/><g stroke="#fff" stroke-width="3" fill="#fff"><line x1="40" y1="34" x2="50" y2="78"/><line x1="56" y1="30" x2="56" y2="80"/><line x1="72" y1="34" x2="62" y2="78"/><circle cx="40" cy="32" r="4"/><circle cx="56" cy="28" r="4"/><circle cx="72" cy="32" r="4"/></g></svg>
    <h3>Dry Needling</h3>
    <p>Lorem ipsum dolor sit amet, consecur adipiscing elit, sed do eiusmod tempor incididunt ut labore et dolore</p>
  </div>
  <div class="service" style="left:355px">
    <svg width="112" height="112" viewBox="0 0 112 112"><circle cx="56" cy="56" r="50" fill="none" stroke="#fff" stroke-width="4"/><path d="M8 70 A50 50 0 0 0 104 70" fill="none" stroke="#fff" stroke-width="8"/><path d="M70 32 L80 42 L48 74 L36 78 L40 66 Z" fill="none" stroke="#fff" stroke-width="4" stroke-linejoin="round"/></svg>
    <h3>Laser &amp; Infrared Therapy</h3>
    <p>Lorem ipsum dolor sit amet, consecur adipiscing elit, sed do eiusmod tempor incididunt ut labore et dolore</p>
  </div>
  <div class="service" style="left:625px">
    <svg width="112" height="112" viewBox="0 0 112 112"><circle cx="56" cy="56" r="50" fill="none" stroke="#fff" stroke-width="4"/><path d="M8 70 A50 50 0 0 0 104 70" fill="none" stroke="#fff" stroke-width="8"/><path d="M46 28 L60 28 L60 60 Q78 64 78 74 Q78 82 66 82 L46 82 Q40 82 40 74 L46 60 Z" fill="none" stroke="#fff" stroke-width="4" stroke-linejoin="round"/></svg>
    <h3>Custom Orthotics</h3>
    <p>Lorem ipsum dolor sit amet, consecur adipiscing elit, sed do eiusmod tempor incididunt ut labore et dolore</p>
  </div>
  <div class="service" style="left:897px">
    <svg width="112" height="112" viewBox="0 0 112 112"><circle cx="56" cy="56" r="50" fill="none" stroke="#fff" stroke-width="4"/><path d="M8 70 A50 50 0 0 0 104 70" fill="none" stroke="#fff" stroke-width="8"/><g fill="#fff"><circle cx="62" cy="34" r="6"/><path d="M30 68 L82 68 L82 74 L30 74 Z"/><path d="M40 62 L58 44 L68 48 L76 62 Z"/></g></svg>
    <h3>Manual Therapy</h3>
    <p>Lorem ipsum dolor sit amet, consecur adipiscing elit, sed do eiusmod tempor incididunt ut labore et dolore</p>
  </div>
</section>

<section class="testimonials">
  <h2 class="section-title">TESTIMONIALS</h2>
  <div class="testimonial" style="left:100px">
    <div class="avatar" role="img" aria-label="Portrait photo of the reviewer"></div>
    <blockquote>" Nemo enim ipsam voluptatem quia voluptas sit ernatur aut odit aut fugit, sed quia consequuntur magni dolores eos qui ratione voluptatem sequi sciunt.</blockquote>
    <p class="name">Dara Whitfield</p>
    <p class="role">Keystone Physical Therapy</p>
    <span class="quote-mark">&rdquo;</span>
  </div>
  <div class="testimonial" style="left:632px">
    <div class="avatar" role="img" aria-label="Portrait photo of the reviewer"></div>
    <blockquote>" Nemo enim ipsam voluptatem quia voluptas sit ernatur aut odit aut fugit, sed quia consequuntur magni dolores eos qui ratione voluptatem sequi sciunt.</blockquote>
    <p class="name">Dara Whitfield</p>
    <p class="role">Keystone Physical Therapy</p>
    <span class="quote-mark">&rdquo;</span>
  </div>
</section>

<h2 class="insurance-title">INSURANCE</h2>
<p class="insurance-text">At Keystone PT, we contract with most insurances. We also have reasonable cash payment options for those who prefer to pay out of pocket. Here is a list of the current insurance carriers that we accept.</p>
<ul class="carrier-list" style="left:346px"><li>Meridian Compcare</li><li>Dept Of Veteran's Affairs</li><li>Worker's Compensation</li></ul>
<ul class="carrier-list" style="left:570px"><li>Auto Claims</li><li>Trustline Life</li><li>Harbor Shield</li></ul>
<ul class="carrier-list" style="left:758px"><li>Harbor Shield Fed</li><li>Northgate Health West</li><li>Serviceplan</li></ul>

<svg class="site-footer" viewBox="0 0 1200 430" preserveAspectRatio="none">
  <path d="M0 20 Q600 -20 1200 20 L1200 430 L0 430 Z" fill="var(--green)"/>
  <path d="M0 30 Q600 -8 1200 30 L1200 430 L0 430 Z" fill="var(--footer)"/>
</svg>

<div class="footer-col" style="left:100px">
  <h4>CONTACT US</h4>
  <p>Keystone Physical Therapy,<br>Ste 200 Marlow Springs, CA</p>
  <div class="contact-row">
    <svg width="18" height="20" viewBox="0 0 26 34"><path d="M6 2 L11 8 L8 13 Q11 21 17 25 L21 21 L25 27 L20 32 Q4 26 2 8 Z" fill="none" stroke="#fff" stroke-width="2"/></svg>
    <p>Call Us +1 555.302.4410<br>(555) - 018 - 2296</p>
  </div>
  <div class="contact-row">
    <svg width="20" height="14" viewBox="0 0 20 14"><rect x="1" y="1" width="18" height="12" fill="none" stroke="#fff" stroke-width="1.5"/><path d="M1 1 L10 8 L19 1" fill="none" stroke="#fff" stroke-width="1.5"/></svg>
    <p>info@brellowkeypt.net</p>
  </div>
</div>
<div class="footer-col" style="left:408px">
  <h4>QUICK LINKS</h4>
  <ul class="quick-links"><li>Home</li><li>About Us</li><li>Services</li><li>Faq</li><li>Forms</li><li>Insurance</li><li>Contact Us</li></ul>
</div>
<div class="footer-col" style="left:644px">
  <h4>OUR LOCATION</h4>
  <div class="map" role="img" aria-label="Street map showing the clinic location"></div>
</div>
<div class="footer-col" style="left:1000px">
  <h4>SOCIAL</h4>
  <ul class="social"><li><span class="ring"></span>Friendwall</li><li><span class="ring"></span>Chirpline</li><li><span class="ring"></span>Circleup</li><li><span class="ring"></span>Clipstream</li></ul>
</div>
<div class="footer-rule"></div>
<p class="copyright">2017 © Copyrights Keystone Physical Therapy.All Rights Reserved</p>

</body>
</html>
```